Flyer for photo scanning business

Hello,
I need a flyer created for my business that would be suitable for print, to drop in letterboxes in my local community.

I would like the flyer to convey very simply the services I offer which is scanning negatives, slides and VHS tapes to digital files.
Hopefully it can make it look like an easy process, as people are often daunted by the task of sorting through old photos so they don't always get around to having them scanned.

I have a pinned facebook post that can be used by the designer to reference my services. Pricing does not need to be included on the flyer.
http://facebook.com/brightvaleimaging

Target Market(s)

Parents & Grandparents

Requirements
Must have
• Must make my services look simple! Refer to pinned facebook post for detailed outline of my services.

I would like to flyer to point towards my contact details -
www.brightvale.com
Margot 0478 219 836

Colours in line with my logo/brand (uploaded to brief).
Nice to have
• Stock images of 35mm film negatives, 8mm film, VHS tapes, or Lumavert slides would be worth including. I have also uploaded a mockup of the USB sticks that I provide with digitised images.
Should not have
• no prices needed,

```html
<!DOCTYPE html>
<html lang="en">
<head>
<meta charset="utf-8">
<title>Brightvale Imaging – Flyer</title>
<link rel="stylesheet" href="https://fonts.googleapis.com/css2?family=Montserrat:wght@400;600;700;800&family=Oswald:wght@600;700&display=swap">
<style>
:root{
  --page:#e6e6e6;
  --paper:#ffffff;
  --paper-grey:#f2f3f5;
  --panel-grey:#f0f1f3;
  --ink:#2b2b2b;
  --text:#3a3a3a;
  --brand:#3a6ea5;
  --brand-mid:#5b8cc0;
  --brand-light:#a9c3de;
  --brand-dark:#2a5589;
  --outline:#1f1f1f;
}
*{margin:0;padding:0;box-sizing:border-box}
html,body{width:1200px;height:2301px;overflow:hidden;background:var(--page)}
body{position:relative;font-family:"Montserrat",sans-serif;color:var(--text)}
.flyer{
  position:absolute;left:0;top:299px;width:782px;height:1110px;
  transform:scale(1.53453);transform-origin:0 0;
  background:var(--paper);overflow:hidden;
}
.top-area{position:absolute;left:0;top:0;width:782px;height:430px;background:var(--paper-grey)}
.divider-band{position:absolute;left:0;top:430px;width:480px;height:9px;background:var(--brand-mid)}
.hero-art{position:absolute;left:0;top:0;width:782px;height:720px}
.brand-mark{position:absolute;left:42px;top:40px;width:214px;text-align:center;color:var(--ink)}
.brand-mark .dot{width:62px;height:62px;border-radius:50%;background:var(--brand-mid);margin:0 auto 18px}
.brand-mark .name{font-size:25px;letter-spacing:6px;font-weight:400;line-height:1}
.brand-mark .sub{display:flex;align-items:center;gap:8px;margin-top:10px;font-size:14px;letter-spacing:4px;font-weight:400}
.brand-mark .sub::before,.brand-mark .sub::after{content:"";flex:1;height:1px;background:var(--brand)}
.headline{position:absolute;left:42px;top:222px;font-family:"Oswald",sans-serif;font-weight:700;line-height:42px;font-size:33px;letter-spacing:.3px}
.headline .l1{color:var(--ink);display:block}
.headline .l2{color:var(--brand);display:block}
.rule{position:absolute;left:42px;top:321px;width:281px;height:2px;background:var(--ink)}
.rule::after{content:"";position:absolute;left:50px;top:-1px;width:50px;height:4px;background:var(--brand)}
.intro{position:absolute;left:42px;top:343px;width:290px;font-size:12.5px;line-height:17.5px;color:var(--text)}
.promise{position:absolute;left:42px;top:463px;width:375px;height:55px;border:1.5px dashed var(--brand);border-radius:7px;padding:9px 18px;font-size:10.8px;font-weight:700;line-height:17px;color:var(--ink);text-transform:uppercase}
.step{position:absolute;left:42px;width:345px}
.step .icon{position:absolute;left:0;top:0;width:86px;height:86px}
.step h3{position:absolute;left:119px;top:0;font-size:16.5px;font-weight:700;color:var(--brand);letter-spacing:.3px}
.step h3 b{color:var(--ink);font-weight:700}
.step p{position:absolute;left:119px;top:27px;width:220px;font-size:12.5px;line-height:16.5px;text-align:justify;color:var(--text)}
.step-1{top:548px}.step-2{top:669px}.step-3{top:800px}
.closing{position:absolute;left:42px;top:962px;width:340px;font-size:12.5px;line-height:17.5px;color:var(--text)}
.tech{position:absolute;left:402px;top:712px;width:380px;height:330px;background:var(--panel-grey);border-radius:8px 0 0 8px;padding:26px 46px 0 14px}
.tech h2{font-size:16.5px;font-weight:700;color:var(--brand);letter-spacing:.4px;margin-bottom:14px}
.tech ul{list-style:none}
.tech li{position:relative;padding-left:40px;font-size:12.5px;line-height:17.5px;text-align:justify;margin-bottom:16px}
.tech li svg{position:absolute;left:8px;top:2px;width:20px;height:20px}
.footer-band{position:absolute;left:0;top:1063px;width:782px;height:47px;background:var(--brand-light)}
.call-block{position:absolute;left:0;top:1041px;width:310px;height:69px}
.call-text{position:absolute;left:42px;top:1046px;color:#fff;line-height:1}
.call-text .label{font-size:19px;font-weight:800;letter-spacing:.3px}
.call-text .phone{font-size:24px;font-weight:600;margin-top:7px;letter-spacing:.5px}
.contact{position:absolute;top:1078px;display:flex;align-items:center;gap:10px;font-size:11px;font-weight:600;color:var(--brand-dark)}
.contact svg{width:13px;height:13px}
.contact-mail{left:318px}.contact-web{left:570px}
</style>
</head>
<body>
<main class="flyer">
  <div class="top-area"></div>

  <svg class="hero-art" viewBox="0 0 782 720" aria-hidden="false">
    <defs>
      <linearGradient id="heroBlue" x1="0" y1="0" x2="1" y2="1">
        <stop offset="0" stop-color="#6f9bcc"/>
        <stop offset="1" stop-color="#4a7bb0"/>
      </linearGradient>
      <linearGradient id="archive" x1="0" y1="0" x2="1" y2="1">
        <stop offset="0" stop-color="#2d3340"/>
        <stop offset=".5" stop-color="#c04a3a"/>
        <stop offset="1" stop-color="#b08558"/>
      </linearGradient>
    </defs>
    <circle cx="706" cy="228" r="358" fill="var(--outline)"/>
    <circle cx="716" cy="224" r="350" fill="url(#heroBlue)" role="img" aria-label="Two branded USB sticks supplied with the digitised files"/>
    <circle cx="557" cy="595" r="103" fill="var(--brand-mid)"/>
    <circle cx="557" cy="595" r="95" fill="url(#archive)" role="img" aria-label="Old film negatives, slides and VHS tapes"/>
  </svg>

  <div class="divider-band"></div>

  <div class="brand-mark">
    <div class="dot"></div>
    <div class="name">BRIGHTVALE</div>
    <div class="sub">IMAGING</div>
  </div>

  <h1 class="headline"><span class="l1">BRIGHTVALE IMAGING</span><span class="l2">IS A SMALL BUSINESS</span></h1>
  <div class="rule"></div>
  <p class="intro">Run from my home in the Perth Hills. I digi-tise photos that haven't been seen in years, bringing them back to life.</p>

  <div class="promise">I promise to make it very easy for you to keep your precious memories forever.</div>

  <section class="step step-1">
    <svg class="icon" viewBox="0 0 86 86">
      <circle cx="43" cy="43" r="40" fill="none" stroke="var(--brand)" stroke-width="1.5" stroke-dasharray="3 3"/>
      <path d="M43 3a40 40 0 0 0 0 80" fill="none" stroke="var(--brand)" stroke-width="2"/>
      <g fill="none" stroke="var(--brand)" stroke-width="2.2" stroke-linejoin="round">
        <rect x="25" y="30" width="14" height="30" rx="2"/>
        <rect x="28" y="25" width="8" height="5"/>
        <path d="M39 35h20v18H39"/>
        <path d="M43 35v18M48 35v18M53 35v18"/>
      </g>
    </svg>
    <h3>STEP <b>01</b></h3>
    <p>Find your old negatives or tapes and organise them as much or as little as you want.</p>
  </section>

  <section class="step step-2">
    <svg class="icon" viewBox="0 0 86 86">
      <circle cx="43" cy="43" r="40" fill="none" stroke="var(--brand)" stroke-width="1.5" stroke-dasharray="3 3"/>
      <path d="M43 3a40 40 0 0 0 0 80" fill="none" stroke="var(--brand)" stroke-width="2"/>
      <g fill="none" stroke="var(--brand)" stroke-width="2.2">
        <circle cx="43" cy="34" r="9"/>
        <path d="M27 60v-4a10 10 0 0 1 10-10h12a10 10 0 0 1 10 10v4z" stroke-linejoin="round"/>
      </g>
    </svg>
    <h3>STEP <b>02</b></h3>
    <p>Contact me here or email margot@brightvale.com and I will come and collect these from your home in the hills area.</p>
  </section>

  <section class="step step-3">
    <svg class="icon" viewBox="0 0 86 86">
      <circle cx="43" cy="43" r="40" fill="none" stroke="var(--brand)" stroke-width="1.5" stroke-dasharray="3 3"/>
      <path d="M43 3a40 40 0 0 0 0 80" fill="none" stroke="var(--brand)" stroke-width="2"/>
      <g fill="none" stroke="var(--brand)" stroke-width="2.2" stroke-linejoin="round">
        <rect x="26" y="26" width="34" height="34" rx="2"/>
        <path d="M26 54l10-10 8 8 6-6 10 10"/>
        <circle cx="51" cy="35" r="3.5"/>
      </g>
    </svg>
    <h3>STEP <b>03</b></h3>
    <p>Once completed (usually within a few days) I will drop back your box of memories with a USB stick containing high resolution JPEG files. Contactless payment will be processed when I arrive.</p>
  </section>

  <p class="closing">High end equipment and my unique technical skills as a TV &amp; Broadcast professional to digitise photo negatives, slides and video tapes.</p>

  <aside class="tech">
    <h2>TECHNICAL THINGS</h2>
    <ul>
      <li><svg viewBox="0 0 20 20"><circle cx="10" cy="10" r="8" fill="none" stroke="var(--brand)" stroke-width="2"/><path d="M6 10l3 3 8-8" fill="none" stroke="var(--brand-dark)" stroke-width="2.4" stroke-linecap="round"/></svg>Every frame is physically cleaned and ex-amined before scanning to ensure the best possible result. I then use an additional in-fra-red scanning technique to further reduce dust and scratches.</li>
      <li><svg viewBox="0 0 20 20"><circle cx="10" cy="10" r="8" fill="none" stroke="var(--brand)" stroke-width="2"/><path d="M6 10l3 3 8-8" fill="none" stroke="var(--brand-dark)" stroke-width="2.4" stroke-linecap="round"/></svg>JPEG files are supplied at 2400 dpi which means you can easily print or enlarge your photos. They also look great on a 4k screen!</li>
      <li><svg viewBox="0 0 20 20"><circle cx="10" cy="10" r="8" fill="none" stroke="var(--brand)" stroke-width="2"/><path d="M6 10l3 3 8-8" fill="none" stroke="var(--brand-dark)" stroke-width="2.4" stroke-linecap="round"/></svg>VHS tapes are upscaled and captured at HD 1080p in a 100% digital workflow ensur-ing the best possibly quality and playback on your computer.</li>
    </ul>
  </aside>

  <div class="footer-band"></div>
  <svg class="call-block" viewBox="0 0 310 69" preserveAspectRatio="none" aria-hidden="true">
    <polygon points="0,0 262,0 310,69 0,69" fill="var(--brand-dark)"/>
  </svg>
  <div class="call-text">
    <div class="label">CALL US</div>
    <div class="phone">0478 219 836</div>
  </div>
  <div class="contact contact-mail">
    <svg viewBox="0 0 14 14"><rect x="1" y="3" width="12" height="8" fill="var(--brand-dark)"/><path d="M1 3l6 5 6-5" fill="none" stroke="var(--brand-light)" stroke-width="1.2"/></svg>
    margot@brightvaleimaging.com
  </div>
  <div class="contact contact-web">
    <svg viewBox="0 0 14 14"><g fill="none" stroke="var(--brand-dark)" stroke-width="1.2"><circle cx="7" cy="7" r="6"/><ellipse cx="7" cy="7" rx="2.6" ry="6"/><path d="M1 7h12M2 4h10M2 10h10"/></g></svg>
    www.brightvale.com
  </div>
</main>
</body>
</html>
```